Plastic surgery office stationary
Larkmere cosmetic surgical group and dr's name is tomas ellingwarde
Plastic surgery office stationary - Medical
Creative Brief
Simple
Larkmere cosmetic surgical group
dr tomas ellingwarde
4172 Corvell blvd suite 3050 Harlow Vale, ca 90214
866 GLO VIDA (866.456.8432)
drtomas@glovidaclinic.com
www.GloVidaClinic.com

```html
<!DOCTYPE html>
<html lang="en">
<head>
<meta charset="utf-8">
<title>Larkmere Cosmetic Surgical Group – Business Card</title>
<link href="https://fonts.googleapis.com/css2?family=Open+Sans:wght@400;600&display=swap" rel="stylesheet">
<style>
  :root {
    --backdrop: #e7e4e1;
    --card: #ffffff;
    --magenta-dark: #8e0f52;
    --magenta: #b81c6f;
    --magenta-light: #d84a93;
    --ink: #3b3b3b;
    --ink-soft: #6a6a6a;
    --divider: #e3d7de;
  }
  * { box-sizing: border-box; margin: 0; padding: 0; }
  html, body {
    width: 1200px; height: 839px; overflow: hidden;
    background: var(--backdrop);
    font-family: "Open Sans", Arial, sans-serif;
  }
  .sheet {
    position: relative; width: 1200px; height: 839px;
    display: flex; align-items: center; justify-content: center; gap: 60px;
  }
  .card {
    position: relative; width: 540px; height: 309px;
    background: var(--card);
    box-shadow: 0 6px 18px rgba(0,0,0,0.18);
    overflow: hidden;
  }
  .band {
    position: absolute; left: 0; right: 0; top: 222px; height: 56px;
    background: linear-gradient(180deg, var(--magenta-light) 0%, var(--magenta) 45%, var(--magenta-dark) 100%);
  }
  .band-line {
    position: absolute; left: 0; right: 0; top: 214px; height: 2px;
    background: var(--magenta);
  }
  .brand {
    display: flex; align-items: center; gap: 12px;
    color: var(--magenta); font-weight: 600;
  }
  .brand-dot {
    width: 16px; height: 16px; border-radius: 50%;
    background: var(--magenta); flex: none;
  }
  .brand-name { line-height: 1.2; text-transform: capitalize; }

  /* front */
  .card--front .brand {
    position: absolute; left: 0; right: 0; top: 92px; justify-content: center;
  }
  .card--front .brand-name { font-size: 22px; }

  /* contact side */
  .contact { position: absolute; left: 30px; top: 36px; color: var(--ink); }
  .contact-name { font-size: 16px; font-weight: 600; margin-bottom: 12px; text-transform: lowercase; }
  .contact-row { display: flex; gap: 9px; font-size: 12px; line-height: 1.45; margin-bottom: 6px; color: var(--ink-soft); }
  .contact-row svg { flex: none; margin-top: 2px; }
  .card--contact .brand {
    position: absolute; left: 290px; top: 92px; width: 230px;
    padding-left: 18px; border-left: 1px solid var(--divider);
  }
  .card--contact .brand-name { font-size: 17px; }
  .website {
    position: absolute; left: 30px; top: 240px;
    color: #fff; font-size: 14px; font-weight: 600; letter-spacing: 0.3px;
  }
</style>
</head>
<body>
<main class="sheet">
  <section class="card card--contact">
    <div class="contact">
      <p class="contact-name">dr tomas ellingwarde</p>
      <div class="contact-row">
        <svg width="11" height="14" viewBox="0 0 11 14"><path d="M5.5 0C2.5 0 0 2.4 0 5.3 0 9.2 5.5 14 5.5 14S11 9.2 11 5.3C11 2.4 8.5 0 5.5 0zm0 7.3a2 2 0 1 1 0-4 2 2 0 0 1 0 4z" fill="var(--magenta)"/></svg>
        <span>4172 Corvell blvd<br>suite 3050<br>Harlow Vale, ca 90214</span>
      </div>
      <div class="contact-row">
        <svg width="11" height="12" viewBox="0 0 12 12"><path d="M2.4 0.5 4.3 3 3.2 4.4c.8 1.7 2.1 3 3.9 3.9L8.5 7l2.6 2-1 2.4C5.2 11.5.6 6.8.5 1.6z" fill="var(--magenta)"/></svg>
        <span>866 GLO VIDA (866.456.8432)</span>
      </div>
      <div class="contact-row">
        <svg width="12" height="10" viewBox="0 0 12 10"><rect x="0.5" y="0.5" width="11" height="9" fill="var(--magenta)"/><path d="M0.5 0.8 6 5.5l5.5-4.7" stroke="#fff" fill="none"/></svg>
        <span>drtomas@glovidaclinic.com</span>
      </div>
    </div>
    <div class="brand">
      <span class="brand-dot"></span>
      <span class="brand-name">Larkmere cosmetic surgical group</span>
    </div>
    <div class="band-line"></div>
    <div class="band"></div>
    <p class="website">www.GloVidaClinic.com</p>
  </section>

  <section class="card card--front">
    <div class="brand">
      <span class="brand-dot"></span>
      <span class="brand-name">Larkmere cosmetic surgical group</span>
    </div>
    <div class="band-line"></div>
    <div class="band"></div>
  </section>
</main>
</body>
</html>
```